Flyer for Self Service Laundromat

I am still not sure what king of flyer or "hand out" to do.
We are about 10 days till opening a self service laundromat

```html
<!DOCTYPE html>
<html lang="es">
<head>
<meta charset="utf-8">
<title>Blue Spin – Gran Apertura</title>
<link rel="stylesheet" href="https://fonts.googleapis.com/css2?family=Roboto:wght@400;500;700;900&family=Open+Sans:wght@400;600;700&display=swap">
<style>
  :root {
    --navy: #2a3593;
    --navy-dark: #1f2878;
    --red: #e3262d;
    --orange: #f26a2b;
    --ink: #333640;
    --white: #ffffff;
    --page: #e8e9eb;
    --photo-light: #f1f2f4;
    --photo-mid: #c9ccd3;
  }
  * { box-sizing: border-box; margin: 0; padding: 0; }
  html, body { width: 1043px; height: 1200px; overflow: hidden; }
  body { background: var(--page); font-family: "Roboto", sans-serif; position: relative; }

  .flyer {
    position: absolute; left: 119px; top: 30px;
    width: 805px; height: 1139px;
    background: var(--white); overflow: hidden;
  }

  /* hero */
  .hero { position: absolute; inset: 0 0 auto 0; height: 400px;
    background: linear-gradient(180deg, #fafafb 0%, var(--photo-light) 100%); }
  .hero-photo { position: absolute; left: 320px; top: 0; width: 485px; height: 400px;
    background: linear-gradient(100deg, #eceef1 0%, #b9c6dc 35%, #aeb3bb 70%, #8e939b 100%); }
  .hero-wave { position: absolute; left: 0; top: 290px; width: 805px; height: 110px; }

  .opening { position: absolute; left: 51px; top: 44px; color: var(--navy);
    font-weight: 900; font-size: 46px; line-height: 46px; letter-spacing: .5px; }
  .opening-note { position: absolute; left: 52px; top: 142px; color: var(--orange);
    font-family: "Open Sans", sans-serif; font-size: 16px; line-height: 20px; font-weight: 600; }

  .badge { position: absolute; left: 52px; top: 244px; width: 134px; height: 130px; }

  /* blue band */
  .band { position: absolute; left: 0; top: 398px; width: 805px; height: 290px;
    background: radial-gradient(ellipse at 50% 35%, #3644a8 0%, var(--navy) 55%, var(--navy-dark) 100%); }
  .brand-title { position: absolute; left: 0; right: 0; top: 90px; text-align: center;
    color: var(--white); font-weight: 900; font-size: 77px; line-height: 80px; letter-spacing: 1px; }
  .brand-sub { position: absolute; left: 0; right: 0; top: 170px; text-align: center;
    color: var(--white); font-weight: 700; font-size: 39px; line-height: 44px; }
  .features { position: absolute; left: 133px; top: 211px; width: 516px; height: 45px;
    background: var(--red); border-radius: 12px; display: flex; justify-content: center;
    align-items: center; gap: 26px; color: var(--white); font-family: "Open Sans", sans-serif;
    font-size: 26px; font-weight: 600; }
  .features li { list-style: none; }
  .features li::before { content: "•"; margin-right: 8px; }

  /* prices */
  .prices { position: absolute; left: 50px; top: 707px; width: 749px; height: 191px;
    border: 2px solid var(--navy); border-radius: 12px; }
  .prices-label { position: absolute; left: 20px; top: 95px; transform: translate(-50%, -50%) rotate(-90deg);
    color: var(--orange); font-weight: 700; font-size: 17px; white-space: nowrap; letter-spacing: .5px; }
  .prices-row { position: absolute; left: 78px; top: 26px; width: 640px; height: 150px; }

  /* contact */
  .visit { position: absolute; left: 50px; top: 928px; color: var(--navy);
    font-weight: 700; font-size: 34px; line-height: 40px; }
  .logo { position: absolute; left: 48px; top: 1000px; width: 118px; display: flex;
    flex-direction: column; align-items: center; gap: 8px; }
  .logo-mark { width: 44px; height: 44px; border-radius: 50%; background: var(--navy); }
  .logo-name { color: var(--navy); font-weight: 700; font-size: 17px; white-space: nowrap; }

  .contacts { position: absolute; left: 171px; top: 995px; list-style: none;
    font-family: "Open Sans", sans-serif; font-size: 18px; color: var(--ink); }
  .contacts li { display: flex; align-items: center; height: 24px; gap: 10px; }
  .contacts svg { width: 18px; height: 18px; flex: none; }

  .location { position: absolute; left: 477px; top: 914px; width: 322px; height: 184px;
    border: 2px solid var(--navy); border-radius: 8px; overflow: hidden; }
  .location-map { position: absolute; inset: 0 0 58px 0;
    background: linear-gradient(135deg, #f4f5f6 0%, #e4e7ea 100%); }
  .location-address { position: absolute; left: 0; right: 0; bottom: 0; height: 58px;
    background: var(--navy); color: var(--white); font-family: "Open Sans", sans-serif;
    font-size: 14px; line-height: 19px; padding: 10px 10px 0 30px; }
  .location-address svg { position: absolute; left: 10px; top: 11px; width: 14px; height: 16px; }

  .footer-bar { position: absolute; left: 0; bottom: 0; width: 805px; height: 19px; background: var(--orange); }
</style>
</head>
<body>
<main class="flyer">

  <section class="hero">
    <div class="hero-photo" role="img" aria-label="Photo of a woman taking clothes out of a front-loading washing machine beside a stack of folded colourful laundry"></div>
    <svg class="hero-wave" viewBox="0 0 805 110" preserveAspectRatio="none" aria-hidden="true">
      <path d="M0 50 C 160 10, 330 0, 470 40 C 600 78, 700 80, 805 60 L805 110 L0 110 Z" fill="#2a3593"/>
    </svg>
    <h1 class="opening">GRAN<br>APERTURA</h1>
    <p class="opening-note">Lavadoras y Secadoras NUEVAS,<br>de Última generación.</p>
    <svg class="badge" viewBox="0 0 134 130" aria-label="Best choice">
      <ellipse cx="67" cy="65" rx="62" ry="58" fill="#fff" stroke="#e3262d" stroke-width="9"/>
      <text x="67" y="60" text-anchor="middle" font-family="Roboto, sans-serif" font-weight="900" font-size="22" fill="#e3262d">BEST</text>
      <text x="67" y="86" text-anchor="middle" font-family="Roboto, sans-serif" font-weight="900" font-size="22" fill="#e3262d">CHOICE</text>
    </svg>
  </section>

  <section class="band">
    <h2 class="brand-title">BLUE SPIN</h2>
    <p class="brand-sub">LAVANDERIAS DE AUTOSERVICIO</p>
    <ul class="features">
      <li>Limpieza</li>
      <li>Rápida</li>
      <li>Accesible</li>
    </ul>
  </section>

  <section class="prices">
    <p class="prices-label">LISTA DE PRECIOS</p>
    <svg class="prices-row" viewBox="0 0 640 150" aria-label="Precios por carga: 8 kg, 13 kg, 15 kg y 23 kg">
      <defs>
        <g id="load">
          <path d="M48 4 L30 12 L18 30 L32 37 L38 29 L38 60 L102 60 L102 29 L108 37 L122 30 L110 12 L92 4 Q70 16 48 4 Z" fill="#fff" stroke="#f26a2b" stroke-width="3" stroke-linejoin="round"/>
          <rect x="6" y="56" width="128" height="11" rx="5" fill="#2a3593"/>
          <path d="M14 70 L126 70 L114 118 L26 118 Z" fill="#2a3593"/>
          <rect x="26" y="79" width="88" height="5" rx="2.5" fill="#fff"/>
          <rect x="29" y="92" width="82" height="5" rx="2.5" fill="#fff"/>
          <rect x="32" y="105" width="76" height="5" rx="2.5" fill="#fff"/>
        </g>
      </defs>
      <g font-family="Roboto, sans-serif" fill="#333640" text-anchor="middle">
        <use href="#load" x="0"/>
        <text x="70" y="42" font-size="14" font-weight="500">8Kg</text>
        <text x="70" y="142" font-size="15">XX,XXY</text>
        <use href="#load" x="166"/>
        <text x="236" y="42" font-size="14" font-weight="500">13Kg</text>
        <text x="236" y="142" font-size="15">XX,XXY</text>
        <use href="#load" x="333"/>
        <text x="403" y="42" font-size="14" font-weight="500">15Kg</text>
        <text x="403" y="142" font-size="15">XX,XXY</text>
        <use href="#load" x="500"/>
        <text x="570" y="42" font-size="14" font-weight="500">23Kg</text>
        <text x="570" y="142" font-size="15">XX,XXY</text>
      </g>
    </svg>
  </section>

  <h2 class="visit">VON A CONOCERNOS</h2>

  <div class="logo">
    <span class="logo-mark"></span>
    <span class="logo-name">Blue Spin</span>
  </div>

  <ul class="contacts">
    <li>
      <svg viewBox="0 0 18 18" aria-hidden="true"><path d="M4 2 L7 2 L8 6 L6 7.5 C7 10 8 11 10.5 12 L12 10 L16 11 L16 14 C16 15 15 16 14 16 C8 16 2 10 2 4 C2 3 3 2 4 2 Z" fill="#f26a2b"/></svg>
      600.214.385 y 611.470.928
    </li>
    <li>
      <svg viewBox="0 0 18 18" aria-hidden="true"><rect x="1.5" y="4" width="15" height="11" rx="1.5" fill="#f26a2b"/><path d="M2.5 5 L9 10 L15.5 5" fill="none" stroke="#fff" stroke-width="1.4"/></svg>
      hola@bluespin-lav.es
    </li>
    <li>
      <svg viewBox="0 0 18 18" aria-hidden="true"><circle cx="9" cy="9" r="7" fill="#f26a2b"/></svg>
      @blue_spin.es
    </li>
    <li>
      <svg viewBox="0 0 18 18" aria-hidden="true"><circle cx="9" cy="9" r="7" fill="none" stroke="#f26a2b" stroke-width="1.6"/><ellipse cx="9" cy="9" rx="3" ry="7" fill="none" stroke="#f26a2b" stroke-width="1.4"/><path d="M2 9 H16" stroke="#f26a2b" stroke-width="1.4"/></svg>
      www.bluespin-lav.es
    </li>
  </ul>

  <div class="location">
    <div class="location-map" role="img" aria-label="Street map showing the laundromat location"></div>
    <p class="location-address">
      <svg viewBox="0 0 14 16" aria-hidden="true"><path d="M7 1 C3.7 1 1.5 3.4 1.5 6.2 C1.5 9.8 7 15 7 15 C7 15 12.5 9.8 12.5 6.2 C12.5 3.4 10.3 1 7 1 Z" fill="#f26a2b"/><circle cx="7" cy="6.2" r="2" fill="#2a3593"/></svg>
      Av. de los Naranjos 12, Bajos,<br>Local Blue Spin. 46990, Vilaclara (Valencia).
    </p>
  </div>

  <div class="footer-bar"></div>
</main>
</body>
</html>
```